【 概要 】 札幌市東区で新築のマンションを竣工しました。2025年5月竣工です。入居者募集チラシの作成をお願いいたします。 近隣マンションにポスティングいたします。 【 依頼内容 】 ・サイズ:A4 片面 ・ページ数:1ページ ・素材の用意(画像・文章等):外観・パース・間取り・室内写真を添付いたします。 外観は必須で記載をお願いいたします。 その他の素材についてはすべて添付が必要というわけではございません。 間取も一部入れていただきたいですが、あまりきれいなデータが無いため小さめに載せていただきたいです。 〇物件名 →クレア彩苑 〇間取 →全室3LDK 全14戸 〇賃料 →127,000円~ 共益費7,000円 〇設備 →都市ガス・オートロック・エアコン・追い焚き・インターネット無料 ペット可(小型犬もしくは猫1匹まで) 敷地内駐車場有(屋内17,600円 屋外14,300円) 〇その他 →24時間管理費1,100円 ※資料としてマイソクも添付いたします。すべての情報の記載が必用というわけではございませんが念のためご確認ください 【 デザインイメージ 】 ・ターゲット層:札幌市在住のファミリー層 札幌市内では賃貸物件の他戸建てのローンと競合する金額のため一定以上の所得がある方がターゲットとなります。 ・雰囲気:新築マンションで、札幌のファミリーマンションの中ではやや高価格帯の物件になるため、 高級感のあるおしゃれなデザインでお願いいたします。 【 契約金額(税抜) 】 3万円 ※契約金額(税込)からシステム利用料を差し引いた金額が、ワーカーさまの受取金額となります その他ご質問等ありましたら、気軽にお問い合わせください。 ご応募をお待ちしております! |
どの案も本当に素敵で、選定が難しかったですが
物件の明るさと清潔感・高級感が伝わるこちらの提案を採用とさせていただきます。
皆様、たくさんのご提案をいただきましてありがとうございました。
本当にどの案も違った魅力がありたくさん悩みました。
またご縁がございましたらご依頼させていただくことがあるかもしれませんので、
その際には何卒よろしくお願いいたします。

```html
<!DOCTYPE html>
<html lang="ja">
<head>
<meta charset="utf-8">
<title>クレア彩苑 入居者募集</title>
<link href="https://fonts.googleapis.com/css2?family=Noto+Serif+JP:wght@500;700;900&family=Noto+Sans+JP:wght@400;500;700;900&display=swap" rel="stylesheet">
<style>
:root{
  --brown:#2f231c;
  --brown-2:#4a382c;
  --gold:#b8955a;
  --gold-light:#d9c08e;
  --cream:#f6f1e8;
  --red:#9b2c1f;
  --ink:#2a2320;
  --white:#ffffff;
}
*{box-sizing:border-box;margin:0;padding:0}
html,body{width:856px;height:1200px;overflow:hidden;background:var(--white)}
body{font-family:"Noto Sans JP",sans-serif;color:var(--ink)}
.flyer{position:relative;width:856px;height:1200px;overflow:hidden;background:var(--white)}
.abs{position:absolute}

/* header */
.header{left:0;top:0;width:856px;height:200px;background:var(--brown)}
.header-photo{left:540px;top:0;width:316px;height:252px;background:linear-gradient(165deg,#f4f2ee 0%,#dcd6cd 45%,#a89c8c 80%,#6e6357 100%);border-left:4px solid var(--gold)}
.tagline-top{left:30px;top:24px;padding:4px 22px;border:1.5px solid var(--gold);color:var(--gold-light);font-family:"Noto Serif JP",serif;font-weight:700;font-size:26px;letter-spacing:.06em}
.title{left:28px;top:70px;font-family:"Noto Serif JP",serif;font-weight:900;font-size:84px;color:var(--white);letter-spacing:.04em;line-height:1.1}
.title-rule{left:30px;top:178px;width:490px;height:3px;background:var(--gold)}
.catch{left:26px;top:212px;font-family:"Noto Serif JP",serif;font-weight:700;font-size:32px;letter-spacing:.04em;color:var(--brown)}

/* rent block */
.rent{left:26px;top:272px;width:355px}
.rent-price{font-family:"Noto Serif JP",serif;font-weight:900;color:var(--red);font-size:26px;line-height:1}
.rent-price strong{font-size:54px;letter-spacing:-.01em}
.rent-fee{margin-top:6px;font-size:15px;font-weight:500}
.rent-fee span{margin-right:12px}
.chips{display:flex;gap:6px;margin-top:10px}
.chip{background:var(--gold);color:var(--white);font-size:12.5px;font-weight:700;padding:4px 8px}
.chip.dark{background:var(--brown-2)}
.plan{margin-top:10px;font-family:"Noto Serif JP",serif;font-weight:900;font-size:40px;color:var(--brown);letter-spacing:.02em}
.plan small{font-size:26px}
.station{margin-top:6px;font-size:13px;line-height:1.5}
.station b{font-size:22px;font-family:"Noto Serif JP",serif;font-weight:700;margin:0 4px}

/* photo grid */
.photos{left:392px;top:262px;width:456px;height:290px;display:grid;grid-template-columns:repeat(3,1fr);grid-template-rows:1fr 1fr;gap:6px}
.photo{border:2px solid var(--white);box-shadow:0 1px 3px rgba(0,0,0,.25)}
.ph1{background:linear-gradient(160deg,#f3f1ed,#d7d0c6 55%,#a59682)}
.ph2{background:linear-gradient(160deg,#efe6d8,#c8b08e 55%,#8a6e4d)}
.ph3{background:linear-gradient(160deg,#f5f3ef,#dcd8d1 50%,#9d978e)}
.ph4{background:linear-gradient(160deg,#e9ebec,#c3c7c9 55%,#8a8f92)}
.ph5{background:linear-gradient(160deg,#f1ece4,#d3c6b3 55%,#9e8a6f)}
.ph6{background:linear-gradient(160deg,#ece7df,#c1b6a6 55%,#7f7264)}

/* diagonal banner */
.banner{left:-40px;top:598px;width:940px;height:112px;background:var(--brown);transform:rotate(-7deg);transform-origin:left top;box-shadow:0 5px 0 var(--gold)}
.banner-inner{left:40px;top:568px;width:860px;height:130px;transform:rotate(-7deg);transform-origin:left bottom}
.completion{left:120px;top:0;background:var(--gold);color:var(--white);font-family:"Noto Serif JP",serif;font-weight:900;font-size:26px;padding:4px 16px}
.birth{left:30px;top:54px;font-family:"Noto Serif JP",serif;font-weight:900;font-size:40px;color:var(--white);letter-spacing:.04em}
.recruit{left:370px;top:30px;font-family:"Noto Serif JP",serif;font-weight:900;font-size:82px;color:var(--white);letter-spacing:.06em;line-height:1}

/* parking + pet */
.parking{left:22px;top:730px;width:270px;height:112px;background:var(--brown);border:2px solid var(--gold);padding:14px 0 0;text-align:center;font-family:"Noto Serif JP",serif;font-weight:900;color:var(--gold-light);font-size:32px;line-height:1.1}
.parking small{display:block;font-family:"Noto Sans JP",sans-serif;font-size:13px;font-weight:500;color:var(--white);margin-top:10px}
.pet-photo{left:300px;top:714px;width:120px;height:120px;border-radius:50%;background:radial-gradient(circle at 45% 40%,#efd8b8,#c4976a 65%,#9c7148);border:4px solid var(--white);box-shadow:0 0 0 2px var(--gold)}
.pet-label{left:314px;top:826px;background:var(--gold);color:var(--white);font-size:13px;font-weight:700;padding:2px 10px;border-radius:12px}

/* features */
.features{left:420px;top:706px;width:430px;height:160px}
.feature{position:absolute;width:92px;height:92px}
.feature svg{position:absolute;inset:0}
.feature span{position:absolute;inset:0;display:flex;align-items:center;justify-content:center;text-align:center;color:var(--white);font-weight:700;font-size:13px;line-height:1.25}

/* building */
.building{left:0;top:862px;width:540px;height:246px;background:linear-gradient(180deg,#dde6ee 0%,#eef1f3 22%,#b9b6b1 40%,#7a726a 70%,#3e3833 100%)}

/* floor plans */
.plans-card{left:546px;top:862px;width:306px;height:140px;background:var(--cream);border:1px solid var(--gold-light)}
.floorplans{left:554px;top:868px;width:292px;display:flex;gap:8px}
.fp{flex:1}
.fp-head{font-size:11px;font-weight:700;color:var(--brown)}
.fp-head b{font-size:14px;color:var(--gold)}
.fp-size{font-family:"Noto Serif JP",serif;font-weight:900;font-size:16px;color:var(--brown)}
.fp-draw{margin-top:4px;height:82px;background:linear-gradient(135deg,#ffffff,#e6e1d9);border:1px solid #8c8276}
.map{left:546px;top:1008px;width:306px;height:98px;background:linear-gradient(135deg,#e8efe1,#d8d9c6 50%,#e6ddd0);border:1px solid var(--gold-light)}
.map-label{left:700px;top:1060px;background:var(--red);color:var(--white);font-size:13px;font-weight:700;padding:3px 10px}
.map-pin{left:682px;top:1054px}

/* footer */
.footer{left:0;top:1110px;width:856px;height:90px;background:var(--white);border-top:3px solid var(--gold)}
.contact{left:24px;top:1118px}
.contact-lead{font-family:"Noto Serif JP",serif;font-weight:900;font-size:19px;color:var(--brown)}
.contact-sub{font-size:11px;margin-top:2px}
.tel{font-family:"Noto Serif JP",serif;font-weight:900;font-size:32px;color:var(--red);line-height:1.1;display:flex;align-items:center;gap:6px}
.tel small{font-size:18px}
.reserve{left:330px;top:1126px}
.reserve-lead{font-size:13px;font-weight:700;color:var(--brown)}
.search{margin-top:6px;display:flex;border:2px solid var(--brown)}
.search span{padding:3px 12px;font-size:14px;font-weight:700}
.search em{font-style:normal;background:var(--brown);color:var(--white);padding:3px 10px;font-size:13px;font-weight:700}
.company{left:600px;top:1124px;width:240px}
.company-name{display:flex;align-items:center;gap:6px;font-weight:700;font-size:14px;color:var(--brown)}
.company-name i{width:14px;height:14px;background:var(--gold);display:inline-block}
.company-mark{font-weight:700;font-size:14px;color:var(--brown);letter-spacing:.1em}
.company-info{font-size:10px;line-height:1.45;margin-top:2px}
</style>
</head>
<body>
<main class="flyer">
  <div class="abs header"></div>
  <div class="abs header-photo" role="img" aria-label="明るいリビングダイニングの室内写真"></div>
  <p class="abs tagline-top">ファミリー向け新築賃貸マンション</p>
  <h1 class="abs title">クレア彩苑</h1>
  <div class="abs title-rule"></div>
  <p class="abs catch">生まれたての家で新しい暮らしを</p>

  <section class="abs rent">
    <p class="rent-price">賃料<strong>127,000</strong>円~</p>
    <p class="rent-fee"><span>共益費7,000円</span><span>24時間管理費1,100円</span></p>
    <div class="chips"><span class="chip">この広さでこの価格!</span><span class="chip dark">ネット無料&amp;都市ガスで経済的</span></div>
    <p class="plan">全室3LDK <small>全14戸</small></p>
    <p class="station">地下鉄東西線「<b>彩苑中央</b>」駅徒歩6分<br>地下鉄東豊線「<b>緑ヶ丘公園</b>」駅徒歩20分</p>
  </section>

  <div class="abs photos">
    <div class="photo ph1" role="img" aria-label="洋室の写真"></div>
    <div class="photo ph2" role="img" aria-label="キッチンの写真"></div>
    <div class="photo ph3" role="img" aria-label="リビングの写真"></div>
    <div class="photo ph4" role="img" aria-label="浴室の写真"></div>
    <div class="photo ph5" role="img" aria-label="洗面台の写真"></div>
    <div class="photo ph6" role="img" aria-label="玄関の写真"></div>
  </div>

  <div class="abs banner"></div>
  <div class="abs banner-inner">
    <p class="abs completion">2025年5月竣工</p>
    <p class="abs birth">ただいま誕生!!</p>
    <p class="abs recruit">入居者募集</p>
  </div>

  <div class="abs parking">敷地内駐車場有<small>(屋内17,600円 屋外14,300円)</small></div>
  <div class="abs pet-photo" role="img" aria-label="小型犬の写真"></div>
  <span class="abs pet-label">ペットと一緒</span>

  <section class="abs features">
    <div class="feature" style="left:10px;top:0"><svg viewBox="0 0 92 92"><polygon points="46,2 90,46 46,90 2,46" fill="#b8955a"/></svg><span>インター<br>ネット<br>無料</span></div>
    <div class="feature" style="left:112px;top:0"><svg viewBox="0 0 92 92"><polygon points="46,2 90,46 46,90 2,46" fill="#4a382c"/></svg><span>ペット<br>可物件</span></div>
    <div class="feature" style="left:214px;top:0"><svg viewBox="0 0 92 92"><polygon points="46,2 90,46 46,90 2,46" fill="#b8955a"/></svg><span>オート<br>ロック</span></div>
    <div class="feature" style="left:316px;top:0"><svg viewBox="0 0 92 92"><polygon points="46,2 90,46 46,90 2,46" fill="#4a382c"/></svg><span>都市ガス</span></div>
    <div class="feature" style="left:163px;top:62px"><svg viewBox="0 0 92 92"><polygon points="46,2 90,46 46,90 2,46" fill="#4a382c"/></svg><span>追い焚き</span></div>
    <div class="feature" style="left:265px;top:62px"><svg viewBox="0 0 92 92"><polygon points="46,2 90,46 46,90 2,46" fill="#b8955a"/></svg><span>エアコン</span></div>
  </section>

  <div class="abs building" role="img" aria-label="4階建てマンションの外観パース"></div>

  <div class="abs plans-card"></div>
  <section class="abs floorplans">
    <div class="fp">
      <p class="fp-head"><b>A</b> TYPE 402号室</p>
      <p class="fp-size">3LDK 72.8㎡</p>
      <div class="fp-draw" role="img" aria-label="Aタイプの間取り図"></div>
    </div>
    <div class="fp">
      <p class="fp-head"><b>B</b> TYPE 101号室</p>
      <p class="fp-size">3LDK 73.1㎡</p>
      <div class="fp-draw" role="img" aria-label="Bタイプの間取り図"></div>
    </div>
  </section>
  <div class="abs map" role="img" aria-label="周辺地図"></div>
  <svg class="abs map-pin" width="16" height="22" viewBox="0 0 16 22"><path d="M8 0a8 8 0 0 0-8 8c0 6 8 14 8 14s8-8 8-14a8 8 0 0 0-8-8z" fill="#9b2c1f"/><circle cx="8" cy="8" r="3" fill="#fff"/></svg>
  <span class="abs map-label">クレア彩苑</span>

  <footer class="abs footer"></footer>
  <div class="abs contact">
    <p class="contact-lead">まずはお気軽にご見学から</p>
    <p class="contact-sub">お電話一本でご案内可能です</p>
    <p class="tel"><svg width="22" height="22" viewBox="0 0 24 24"><path d="M6.6 10.8a15 15 0 0 0 6.6 6.6l2.2-2.2a1 1 0 0 1 1-.25 11.4 11.4 0 0 0 3.6.57 1 1 0 0 1 1 1V20a1 1 0 0 1-1 1A17 17 0 0 1 3 4a1 1 0 0 1 1-1h3.5a1 1 0 0 1 1 1c0 1.25.2 2.45.57 3.57a1 1 0 0 1-.25 1z" fill="#9b2c1f"/></svg><small>TEL</small>011-555-0148</p>
  </div>
  <div class="abs reserve">
    <p class="reserve-lead">アプリ・WEBで簡単予約</p>
    <div class="search"><span>クレア彩苑</span><em>検索</em></div>
  </div>
  <div class="abs company">
    <p class="company-name"><i></i>株式会社 緑陽ビルグループ</p>
    <p class="company-mark">RYOYO</p>
    <p class="company-info">北海道札幌市中央区南一条西1丁目2-3<br>TEL 011-555-0148 FAX 011-555-0149</p>
  </div>
</main>
</body>
</html>
```